Visitenkarten-Design für Rechtsanwälte
Zielgruppe
Wir sind eine Rechtsanwaltskanzlei. Die Visitenkarten werden vor allem an Mandanten, also Rechtssuchende, verteilt.
www.bsp-anwalt.de
Aufgabenstellung
Unsere Visitenkarte soll weiterhin seriös wirken, aber moderner werden. Gegenüber der bisherigen Visitenkarte, siehe erster Anhang, stellen wir uns einen doppelseitigen Druck und evtl. etwas Farbe vor. Auf der einen Seite sollte nur noch der Name der Kanzlei stehen, der inzwischen etwas länger ist: Brenninger, Stadler & Partner - Rechtsanwälte Partnerschaftsgesellschaft mbB, mit Kontaktdaten. Auf der Rückseite dann der Name und ggf. Daten zu dem einzelnen Anwalt, z.B. Dr. Henrike Lorenz, Rechtsanwältin, Fachanwältin für Medizinrecht, Mediatorin ebZAV, Kontaktdaten.
Unser aktueller Briefkopf ist als zweiter Anhang beigefügt.
Unsere Homepage ist: www.bsp-anwalt.de - Der dortige Look könnte sich auf den Visitenkarten wiederfinden, was die mögliche Farbe(n) angeht, also weinrot oder/und blau.
Ein insgesamt neues Corporate Design für den gesamten Auftritt ist mittelfristig geplant, im Moment brauchen wir nur neue, modernere Visitenkarten.

```html
<!DOCTYPE html>
<html lang="de">
<head>
<meta charset="utf-8">
<title>Visitenkarte – Brenninger, Stadler &amp; Partner</title>
<link href="https://fonts.googleapis.com/css2?family=Open+Sans:wght@400;700&display=swap" rel="stylesheet">
<style>
  :root {
    --backdrop: #e6e2dc;
    --paper: #ffffff;
    --wine: #a8121b;
    --ink: #1b1b1b;
  }
  * { margin: 0; padding: 0; box-sizing: border-box; }
  html, body { width: 1200px; height: 822px; overflow: hidden; }
  body {
    background: var(--backdrop);
    font-family: "Open Sans", Arial, sans-serif;
    color: var(--ink);
    position: relative;
  }
  .card {
    position: absolute;
    width: 520px;
    height: 336px;
    background: var(--paper);
    box-shadow: 0 6px 18px rgba(0,0,0,.18);
    overflow: hidden;
  }
  .card--front { left: 70px; top: 60px; }
  .card--back  { left: 610px; top: 426px; }

  /* front */
  .firm {
    position: absolute;
    left: 0; right: 0; top: 112px;
    text-align: center;
  }
  .firm__name {
    color: var(--wine);
    font-weight: 700;
    font-size: 27px;
    letter-spacing: .2px;
    line-height: 1.15;
  }
  .firm__line {
    font-size: 16px;
    line-height: 1.35;
    margin-top: 2px;
  }

  /* back */
  .person {
    position: absolute;
    left: 58px; top: 178px;
    text-align: center;
  }
  .person__name {
    color: var(--wine);
    font-weight: 700;
    font-size: 22px;
    line-height: 1.15;
  }
  .person__role {
    font-size: 13px;
    line-height: 1.35;
  }
  .divider {
    position: absolute;
    left: 298px; top: 92px;
    width: 1.5px; height: 118px;
    background: var(--wine);
  }
  .contact {
    position: absolute;
    left: 328px; top: 100px;
    list-style: none;
  }
  .contact__item {
    display: flex;
    align-items: center;
    gap: 9px;
    font-size: 13px;
    line-height: 22px;
  }
  .contact__icon { width: 12px; height: 12px; fill: var(--wine); flex: none; }
  .address {
    position: absolute;
    right: 26px; bottom: 26px;
    font-size: 13px;
  }
  .band {
    position: absolute;
    left: 0; right: 0; bottom: 0;
    height: 7px;
    background: var(--wine);
  }
</style>
</head>
<body>

<section class="card card--front" aria-label="Vorderseite">
  <div class="firm">
    <div class="firm__name">Brenninger, Stadler &amp; Partner</div>
    <div class="firm__line">Rechtsanwälte</div>
    <div class="firm__line">Partnerschaftsgesellschaft mbB</div>
  </div>
</section>

<section class="card card--back" aria-label="Rückseite">
  <div class="person">
    <div class="person__name">Dr. Henrike Lorenz</div>
    <div class="person__role">Rechtsanwältin</div>
    <div class="person__role">Fachanwältin für Medizinrecht</div>
  </div>

  <div class="divider"></div>

  <ul class="contact">
    <li class="contact__item">
      <svg class="contact__icon" viewBox="0 0 24 24" aria-hidden="true"><path d="M6.6 10.8a15.1 15.1 0 0 0 6.6 6.6l2.2-2.2c.3-.3.7-.4 1-.2 1.1.4 2.3.6 3.6.6.6 0 1 .4 1 1V20c0 .6-.4 1-1 1A17 17 0 0 1 3 4c0-.6.4-1 1-1h3.5c.6 0 1 .4 1 1 0 1.3.2 2.5.6 3.6.1.3 0 .7-.2 1z"/></svg>
      (0711) 48 62 9 - 0
    </li>
    <li class="contact__item">
      <svg class="contact__icon" viewBox="0 0 24 24" aria-hidden="true"><path d="M6 2h12v6H6zM3 9h18a2 2 0 0 1 2 2v6h-5v5H6v-5H1v-6a2 2 0 0 1 2-2zm5 8v3h8v-3z"/></svg>
      (0711) 48 62 9 - 33
    </li>
    <li class="contact__item">
      <svg class="contact__icon" viewBox="0 0 24 24" aria-hidden="true"><path d="M2 5h20v14H2zm2 2v.5l8 5.5 8-5.5V7zm0 3v7h16v-7l-8 5.5z"/></svg>
      lorenz@bsp-anwalt.de
    </li>
    <li class="contact__item">
      <svg class="contact__icon" viewBox="0 0 24 24" aria-hidden="true"><path d="M12 2a10 10 0 1 0 0 20 10 10 0 0 0 0-20zm-1 17.9A8 8 0 0 1 4.2 10l4.8 4.8v1a2 2 0 0 0 2 2zm6.9-2.5a2 2 0 0 0-1.9-1.4h-1v-3a1 1 0 0 0-1-1H8v-2h2a1 1 0 0 0 1-1V7h2a2 2 0 0 0 2-2v-.4a8 8 0 0 1 2.9 12.8z"/></svg>
      www.bsp-anwalt.de
    </li>
  </ul>

  <div class="address">Brenninger, Stadler &amp; Partner, Kastanienweg 7, 70176 Stuttgart</div>
  <div class="band"></div>
</section>

</body>
</html>
```